Business Card design for new private practice opening

I need a business card design for my new private practice with my new logo uploaded as a file
On the front the logo
On the back: maybe a small logo somewhere?
Priv. Doz. DDr. Corinna Vestaluk
Fachärztin für Allgemein- & Viszeralchirurgie
Address: xxx
Tel: xxx
Mobil:xxx
Webseite:xxx
Email:xxx

Contact Information for Business Card

See project description above for details

Requirements
Nice to have
• I would like the colors of the logo incorporated into the business card

```html
<!DOCTYPE html>
<html lang="de">
<head>
<meta charset="utf-8">
<title>Vestaluk Chirurgie – Visitenkarte</title>
<link href="https://fonts.googleapis.com/css2?family=Mulish:wght@400;500;700;800&display=swap" rel="stylesheet">
<style>
  :root{
    --bg:#e4e6e5;
    --card-front:#f4f4f4;
    --card-back:#7b7b7b;
    --pattern-light:#888888;
    --pattern-dark:#727272;
    --teal:#3aa9a5;
    --ink:#4a4a4a;
    --ring:#7f7f7f;
    --light-text:#ececec;
  }
  *{margin:0;padding:0;box-sizing:border-box}
  html,body{width:1200px;height:1200px;overflow:hidden}
  body{background:var(--bg);font-family:"Mulish",Arial,sans-serif;position:relative}
  .card{position:absolute;left:235px;width:730px;height:417px;border-radius:4px;box-shadow:0 10px 24px rgba(0,0,0,.18)}
  .card--front{top:140px;background:var(--card-front)}
  .card--back{top:620px;background:var(--card-back);overflow:hidden}

  .holder{position:absolute;left:69px;top:50px}
  .holder__name{color:var(--teal);font-weight:800;font-size:25px;letter-spacing:.2px}
  .holder__title{color:var(--ink);font-size:17px;margin-top:2px;font-weight:500}

  .address{position:absolute;left:69px;top:180px;color:var(--ink);font-size:17px;line-height:26px;font-weight:500}

  .contacts{position:absolute;left:69px;top:260px;list-style:none}
  .contacts li{display:flex;align-items:center;height:26px;color:var(--ink);font-size:17px;font-weight:500}
  .contacts li.contacts__phone{font-size:18px}
  .contacts svg{width:16px;height:16px;margin-right:10px;flex:none}

  .practice-mark{position:absolute;left:472px;top:176px;width:200px;display:flex;flex-direction:column;align-items:center}
  .practice-mark__disc{width:110px;height:110px;border-radius:50%;background:var(--teal)}
  .practice-mark__name{margin-top:14px;color:var(--teal);font-weight:800;font-size:17px;letter-spacing:1px;text-align:center;line-height:21px}

  .back-pattern{position:absolute;inset:0;background:linear-gradient(135deg,var(--pattern-light),var(--pattern-dark))}
  .back-brand{position:absolute;left:410px;top:258px;display:flex;align-items:center}
  .back-brand__disc{width:70px;height:70px;border-radius:50%;background:var(--teal);border:4px solid var(--light-text);margin-right:12px;flex:none}
  .back-brand__name{color:var(--light-text);font-weight:700;font-size:24px;line-height:27px;letter-spacing:.5px}
</style>
</head>
<body>

<section class="card card--front">
  <div class="holder">
    <h1 class="holder__name">Priv. Doz. DDr. Corinna Vestaluk</h1>
    <p class="holder__title">Fachärztin für Allgemein- &amp; Viszeralchirurgie</p>
  </div>

  <address class="address" style="font-style:normal">
    Lindenweg 17, Kellbach<br>Rheinland-Pfalz
  </address>

  <ul class="contacts">
    <li class="contacts__phone">
      <svg viewBox="0 0 16 16"><path d="M3 1.5l2.5 0 1 3.5-1.6 1.2a8 8 0 0 0 4.9 4.9L11 9.5l3.5 1v2.5c0 .8-.7 1.5-1.5 1.5C7 14.5 1.5 9 1.5 3c0-.8.7-1.5 1.5-1.5z" fill="var(--teal)"/></svg>
      (214) 73916
    </li>
    <li class="contacts__phone">
      <svg viewBox="0 0 16 16"><rect x="3.5" y="0.8" width="9" height="14.4" rx="1.6" fill="var(--teal)"/><rect x="5" y="2.6" width="6" height="9" fill="var(--card-front)"/><circle cx="8" cy="13.3" r=".8" fill="var(--card-front)"/></svg>
      (214) 608257
    </li>
    <li>
      <svg viewBox="0 0 16 16"><rect x="1" y="3" width="14" height="10" rx="1" fill="var(--teal)"/><path d="M1.8 4l6.2 4.8L14.2 4" stroke="var(--card-front)" stroke-width="1.4" fill="none"/></svg>
      info@vestalukchirurgie.com
    </li>
    <li>
      <svg viewBox="0 0 16 16"><circle cx="8" cy="8" r="7" fill="var(--teal)"/><g stroke="var(--card-front)" stroke-width="1" fill="none"><ellipse cx="8" cy="8" rx="3" ry="7"/><path d="M1 8h14M2 4.5h12M2 11.5h12"/></g></svg>
      www.vestalukchirurgie.com
    </li>
  </ul>

  <div class="practice-mark">
    <div class="practice-mark__disc"></div>
    <p class="practice-mark__name">VESTALUK<br>CHIRURGIE</p>
  </div>
</section>

<section class="card card--back">
  <div class="back-pattern" role="img" aria-label="Repeating embossed pattern of the practice emblem across the card back"></div>
  <div class="back-brand">
    <div class="back-brand__disc"></div>
    <p class="back-brand__name">VESTALUK<br>CHIRURGIE</p>
  </div>
</section>

</body>
</html>
```